Modern Web Design for Nonprofit Organization

Our client is looking to redesign their website. They want a modern look, clean and professional, that integrates their new brand guidelines.

Here is clients current site:
http://www.valorandes.org/

They want their own unique design but here are some sites the clients likes:
https://www.brixtonvane.com/en/
https://oakhollowrise.org/
https://www.lumacraft.com/
https://www.tbnlawgroup.com/
https://www.greyharborco.org/

Attached please find the clients logos, color palette, site plan and design specs.

You will create a homepage mockup that will have the following sections in this order:
1. Thin Alert Bar at very top with one line message
2. Nav Bar with Logo and Main Nav (red in site plan)
3. Hero Image or Video
4. Signup Bar with name email and zip and connect button
5. Intro section with image, welcome message, and supporter counter
6. Featured Action section with call to action
7. Event section with two upcoming event cards
8. Latest News section with three latest blog post
9. Support our work (donation) section
10. Worker and Member Stories Section with feed of social posts
11. Footer.

You can use text and images from clients existing site or placeholder images and placeholder text.

Please submit as many home page mockups/idea boards as you like. Client will pick the top three and ask for some revisions. If you are selected this will lead to a lot of work for this client.

Project is private please adhere to ArtPlenary terms of use and do not share any materials please.

QUICKEST RESPONSE PLEASE!

Thanks for looking!

Target Market(s)

Non profit donors and farmworker advocates

Number of Pages Required

2 page

Font styles to use
Sans Serif

Requirements
Must have
• Adhere to brief and client brand ID
Nice to have
• World class design

```html
<!DOCTYPE html>
<html lang="en">
<head>
<meta charset="utf-8">
<title>Campo Foundation – Join the Farm Worker Movement</title>
<link href="https://fonts.googleapis.com/css2?family=Poppins:wght@400;500;600;700&family=Open+Sans:wght@400;600;700&display=swap" rel="stylesheet">
<style>
:root{
  --blue:#2b3fc8;
  --blue-dark:#1f2f9e;
  --red:#e01b1b;
  --navy:#232a3e;
  --ink:#222;
  --grey:#666;
  --light:#f3f4f8;
  --white:#fff;
}
*{box-sizing:border-box;margin:0;padding:0}
html,body{width:1200px;height:5333px;overflow:hidden}
body{font-family:"Open Sans",sans-serif;color:var(--ink);background:var(--white);position:relative}
h1,h2,h3,h4,.heading{font-family:"Poppins",sans-serif}
.abs{position:absolute}
.photo{position:absolute}
.btn{display:inline-flex;align-items:center;justify-content:center;font-family:"Poppins",sans-serif;font-weight:600}

/* alert bar */
.alert-bar{left:0;top:0;width:1200px;height:34px;background:var(--blue);color:#fff;font-size:12px}
.alert-bar .msg{position:absolute;left:112px;top:9px}
.alert-bar .util{position:absolute;left:616px;top:8px;display:flex;gap:18px;font-weight:600;font-size:12px}
.alert-bar .util span+span{border-left:1px solid rgba(255,255,255,.5);padding-left:18px}
.lang{position:absolute;left:936px;top:7px;width:152px;height:20px;background:#fff;color:#888;font-size:10px;padding:3px 8px;border-radius:2px}

/* nav */
.nav{left:0;top:34px;width:1200px;height:104px;background:#fff;border-bottom:1px solid #e6e6e6}
.brand{position:absolute;display:flex;align-items:center;gap:10px}
.brand .dot{width:62px;height:62px;border-radius:50%;background:var(--red)}
.brand .name{font-family:"Poppins",sans-serif;font-weight:700;line-height:1.05;font-size:19px;color:var(--ink)}
.nav .brand{left:112px;top:22px}
.nav .links{position:absolute;left:510px;top:45px;display:flex;gap:36px;font-size:13px;color:#555}
.nav .donate{position:absolute;left:964px;top:36px;width:124px;height:36px;background:var(--blue);color:#fff;font-size:15px;border-radius:3px}

/* hero */
.hero-photo{left:0;top:138px;width:1200px;height:530px;background:linear-gradient(110deg,#5d7a3a 0%,#8ca25c 40%,#b9a88a 70%,#7c6a52 100%)}
.hero-card{left:112px;top:240px;width:598px;height:331px;background:var(--red);color:#fff;padding:42px 56px}
.hero-card h1{font-size:42px;line-height:1.12;font-weight:700}
.hero-card p{font-size:18px;margin-top:20px;line-height:1.35;max-width:460px}
.hero-card .btn{margin-top:24px;width:192px;height:54px;background:#fff;color:var(--ink);font-size:17px;border-radius:3px}

/* signup */
.signup{left:0;top:668px;width:1200px;height:225px;background:var(--blue);color:#fff}
.signup h2{position:absolute;left:0;width:1200px;text-align:center;top:36px;font-size:30px;font-weight:600}
.field{position:absolute;top:112px;font-size:12px}
.field .box{margin-top:6px;height:34px;background:#fff;border-radius:2px}
.signup .go{position:absolute;left:540px;top:128px;width:120px;height:34px;background:var(--red);color:#fff;font-size:12px}
.signup .divider{position:absolute;left:686px;top:100px;width:1px;height:100px;background:rgba(255,255,255,.55)}
.signup .text{position:absolute;left:716px;top:98px;width:380px;font-size:12px;line-height:1.6}
.signup .text strong{display:block;font-size:16px;font-weight:400;margin-bottom:10px}
.signup .text small{display:block;font-size:10px;opacity:.85;line-height:1.7}

/* video tiles */
.video{top:993px;height:417px}
.video .cap{position:absolute;left:0;bottom:0;width:100%;height:88px;background:linear-gradient(90deg,rgba(224,27,27,.95),rgba(224,27,27,.55));color:#fff;font-family:"Poppins",sans-serif;font-weight:600;font-size:20px;line-height:1.3;padding:16px 0 0 112px}
.video .cap::before{content:"";position:absolute;left:96px;top:16px;width:2px;height:56px;background:#fff}
.play{position:absolute;width:78px;height:78px;border-radius:50%;background:#fff}
.play svg{position:absolute;left:27px;top:22px}

/* help */
.help-bg{left:0;top:1650px;width:1200px;height:412px;background:linear-gradient(180deg,#f4f5f9,#dcdfe8)}
.help h2{position:absolute;left:0;top:1500px;width:1200px;text-align:center;font-size:40px;font-weight:600}
.card{position:absolute;top:1650px;width:225px;height:308px;background:var(--blue);color:#fff;text-align:center;padding-top:26px}
.card .ico{width:86px;height:86px;border-radius:50%;background:#fff;margin:0 auto;display:flex;align-items:center;justify-content:center}
.card h3{font-size:17px;font-weight:600;margin-top:22px}
.card p{font-size:12.5px;line-height:2.2;margin-top:2px;padding:0 34px}
.card .btn{position:absolute;left:48px;bottom:22px;width:128px;height:34px;background:#fff;color:var(--ink);font-size:12px;font-weight:500}

/* events */
.events{left:0;top:2062px;width:1200px;height:663px;background:linear-gradient(100deg,#2a8fb4 0%,#2a6fc0 40%,#2b4fc8 100%)}
.events h2{position:absolute;top:2064px;color:#fff;font-size:28px;font-weight:600}
.recent-photo{left:112px;top:2180px;width:402px;height:355px;background:linear-gradient(160deg,#6a78c8,#3e4fa8 55%,#2b3a86)}
.recent-cap{left:112px;top:2425px;width:402px;height:110px;background:rgba(34,40,96,.75);color:#fff;padding:16px 22px}
.recent-cap h3{font-size:20px;font-weight:600;line-height:1.25}
.recent-cap .meta{margin-top:10px;font-size:11px;display:flex;gap:20px}
.thumb{position:absolute;top:2545px;width:93px;height:85px;background:linear-gradient(160deg,#4d5a9e,#222c5e)}
.tabs{left:538px;top:2183px;height:44px;display:flex}
.tab{height:44px;display:flex;align-items:center;padding:0 20px;font-size:12px;font-weight:700;font-family:"Poppins",sans-serif}
.tab.on{background:#fff;color:var(--ink);width:136px}
.tab.off{background:var(--red);color:#fff;width:114px;justify-content:center}
.schedule{left:538px;top:2227px;width:550px;height:410px;background:#fff;padding:20px 0 0 28px}
.item{display:flex;height:99px}
.item .date{width:100px;font-size:13px;color:var(--red)}
.item .date span{display:block;color:#888}
.item .pic{width:72px;height:66px;background:linear-gradient(150deg,#c9b59a,#6b7fb8)}
.item .info{margin-left:14px;font-family:"Poppins",sans-serif;font-weight:600;font-size:15px;line-height:1.25;width:230px}
.item .info small{display:block;font-family:"Open Sans",sans-serif;font-weight:400;color:#888;font-size:11px;margin-top:8px}
.item .info small::before{content:"";display:inline-block;width:7px;height:7px;border-radius:50%;background:var(--red);margin-right:6px}

/* blog */
.blog-kicker{left:0;top:2778px;width:1200px;text-align:center;font-size:30px;color:#777}
.blog-title{left:0;top:2820px;width:1200px;text-align:center;font-size:40px;font-weight:700}
.post{position:absolute;width:308px;height:253px}
.post.text{border:1px solid #ddd;padding:16px 14px;background:#fff}
.post h3{font-size:16px;font-weight:600;line-height:1.3}
.post .date{font-size:11px;color:#888;margin-top:12px}
.post p{font-size:10px;color:#777;line-height:1.95;margin-top:8px}
.post .more{font-size:11px;color:var(--red);margin-top:6px}

/* donate band */
.band{left:0;top:3600px;width:1200px;height:240px;background:var(--blue);color:#fff}
.band .logo{position:absolute;left:112px;top:36px;text-align:center;width:168px}
.band .logo .dot{width:96px;height:96px;border-radius:50%;background:var(--red);margin:0 auto}
.band .logo b{display:block;font-family:"Poppins",sans-serif;font-size:17px;margin-top:10px}
.band .logo span{font-size:16px}
.band .slogan{position:absolute;left:330px;top:108px;font-size:20px}
.band .btn{position:absolute;left:893px;top:90px;width:192px;height:56px;background:var(--red);color:#fff;font-size:19px;border-radius:3px}

/* stories */
.stories-bg{left:0;top:3840px;width:1200px;height:790px;background:linear-gradient(180deg,#eceef5,#f6f7fb)}
.stories h2{position:absolute;left:0;top:3934px;width:1200px;text-align:center;font-size:40px;font-weight:600}

/* partners */
.movement{left:0;top:4690px;width:1200px;text-align:center;font-family:"Poppins",sans-serif;font-size:30px;font-weight:600;letter-spacing:3px;color:#777}
.badge{position:absolute;top:4770px;height:60px;background:#c62828}

/* footer */
.footer{left:0;top:4895px;width:1200px;height:438px;background:var(--navy);color:#fff}
.footer .brand{left:112px;top:50px}
.footer .brand .dot{width:74px;height:74px}
.footer .brand .name{color:#fff;font-size:20px}
.footer .about{position:absolute;left:112px;top:158px;width:260px;font-size:12px;line-height:1.75;color:#dfe2ea}
.footer h4{position:absolute;top:72px;font-size:18px;font-weight:500}
.footer .links{position:absolute;left:560px;top:130px;font-size:12px;line-height:31px;color:#dfe2ea}
.contact{position:absolute;left:874px;display:flex;gap:14px;font-size:12px;line-height:1.6;color:#dfe2ea}
.social{position:absolute;left:874px;top:260px;display:flex;gap:22px}
.social span{width:22px;height:22px;background:#fff;border-radius:3px}
.footer .copy{position:absolute;left:112px;top:410px;font-size:12px;color:#dfe2ea}
</style>
</head>
<body>

<!-- alert bar -->
<div class="abs alert-bar">
  <div class="msg">Join the movement of worker and human Kind</div>
  <div class="util"><span>Employment</span><span>Membership</span><span>Log in</span></div>
  <div class="lang">Select Language ▾</div>
</div>

<!-- navigation -->
<header class="abs nav">
  <div class="brand"><div class="dot"></div><div class="name">CAMPO<br>FOUNDATION</div></div>
  <nav class="links"><span>About us</span><span>Immigraiton</span><span>Programs</span><span>Join us</span><span>Blog</span></nav>
  <div class="btn donate">Donate</div>
</header>

<!-- hero -->
<div class="photo hero-photo" role="img" aria-label="Smiling farm worker woman in a red shirt standing in a vineyard"></div>
<section class="abs hero-card">
  <h1>Join the Farm worker Movement</h1>
  <p>Essential farm worker Project,Financial assistance for farm worker</p>
  <div class="btn">Donate Now</div>
</section>

<!-- signup -->
<section class="abs signup">
  <h2>Stay Connected with us!</h2>
  <div class="field" style="left:112px;width:122px">Full Name<div class="box"></div></div>
  <div class="field" style="left:248px;width:138px">Email Address<div class="box"></div></div>
  <div class="field" style="left:401px;width:122px">Zip Code<div class="box"></div></div>
  <div class="btn go">Sign up</div>
  <div class="divider"></div>
  <div class="text"><strong>Sign Up With Text</strong>Text "PAPELES" to 555-010<small>CF does not charge for text messages but your phone company may apply charges according to your plan</small></div>
</section>

<!-- video tiles -->
<div class="photo video" style="left:0;width:587px;background:linear-gradient(150deg,#7f9a6a,#a08466 60%,#6f5a44)" role="img" aria-label="Farm worker in a cap in the field, video thumbnail">
  <div class="play" style="left:294px;top:134px"><svg width="28" height="34"><path d="M0 0L28 17L0 34Z" fill="#2b3fc8"/></svg></div>
  <div class="cap">Why Farmworkers don't get paid overtime<br>who pick your Food?</div>
</div>
<div class="photo video" style="left:610px;width:590px;background:linear-gradient(150deg,#8db8a6,#5f8f80 55%,#b84a3a)" role="img" aria-label="Young woman in a red headscarf, video thumbnail">
  <div class="play" style="left:266px;top:150px"><svg width="28" height="34"><path d="M0 0L28 17L0 34Z" fill="#2b3fc8"/></svg></div>
  <div class="cap" style="font-size:19px;padding-left:42px">A african Immigrant Story<br><span style="font-weight:400">In the Land of the Free</span></div>
</div>

<!-- help -->
<section class="help">
  <div class="photo help-bg" role="img" aria-label="Faded crowd of workers at a rally"></div>
  <h2>Help to solve worker Problem</h2>
  <div class="card" style="left:112px"><div class="ico"><svg width="44" height="44" fill="none" stroke="#2b3fc8" stroke-width="2.5"><rect x="6" y="6" width="28" height="16" rx="2"/><circle cx="20" cy="14" r="4"/><path d="M4 36h10l8 4 14-8"/></svg></div><h3>Donate Today</h3><p>Pay safe secure way through via credit card or PayNest</p><div class="btn">Donate Now</div></div>
  <div class="card" style="left:362px"><div class="ico"><svg width="44" height="44" fill="none" stroke="#2b3fc8" stroke-width="2.5"><rect x="6" y="8" width="32" height="30" rx="2"/><path d="M6 16h32M14 4v8M30 4v8M12 22h4M20 22h4M28 22h4M12 30h4M20 30h4M28 30h4"/></svg></div><h3>Donate Monthly</h3><p>Keep Helping worker and Immigrant for a year</p><div class="btn">Donate Monthly</div></div>
  <div class="card" style="left:612px"><div class="ico"><svg width="44" height="44" fill="none" stroke="#2b3fc8" stroke-width="2.5"><circle cx="22" cy="12" r="6"/><path d="M10 38v-8a12 12 0 0124 0v8M22 22v16"/></svg></div><h3>Fundraise</h3><p style="line-height:1.7;margin-top:10px">Create a Personal Fundraising Campaign</p><div class="btn">Contact us</div></div>
  <div class="card" style="left:864px"><div class="ico"><svg width="44" height="44" fill="none" stroke="#2b3fc8" stroke-width="2.5"><circle cx="12" cy="14" r="4"/><circle cx="22" cy="10" r="4"/><circle cx="32" cy="14" r="4"/><path d="M6 38V26a6 6 0 0112 0M16 38V22a6 6 0 0112 0v16M26 26a6 6 0 0112 0v12"/></svg></div><h3>Volunteer</h3><p>Give your time and Help Community</p><div class="btn">Be Volunteer</div></div>
</section>

<!-- events -->
<section class="abs events"></section>
<h2 class="abs" style="left:112px;top:2126px;color:#fff;font-size:28px;font-weight:600;font-family:Poppins,sans-serif">Recent Event</h2>
<h2 class="abs" style="left:538px;top:2122px;color:#fff;font-size:28px;font-weight:600;font-family:Poppins,sans-serif">Upcoming Schedules</h2>
<div class="photo recent-photo" role="img" aria-label="Audience seated at a foundation meetup event"></div>
<div class="abs recent-cap"><h3>CAMPO Foundation Meet up Event</h3><div class="meta"><span>▣ 20 Photo</span><span>▶ 5 Video</span></div></div>
<div class="thumb" style="left:112px" role="img" aria-label="Event crowd photo"></div>
<div class="thumb" style="left:215px" role="img" aria-label="Event crowd photo"></div>
<div class="thumb" style="left:318px" role="img" aria-label="Event crowd photo"></div>
<div class="thumb" style="left:421px" role="img" aria-label="Event crowd photo"></div>
<div class="abs tabs"><div class="tab on">NEXT EVENT</div><div class="tab off">METTING</div></div>
<div class="abs schedule">
  <div class="item"><div class="date">30 NOV 2020<span>03:00PM</span></div><div class="pic" role="img" aria-label="Marathon runners"></div><div class="info">Annual Merathon 2020 for Donation<small>Mayor office,new joursy</small></div></div>
  <div class="item"><div class="date">30 NOV 2020<span>03:00PM</span></div><div class="pic" role="img" aria-label="Marathon runners"></div><div class="info">Annual Merathon 2020 for Donation<small>Mayor office,new joursy</small></div></div>
  <div class="item"><div class="date">30 NOV 2020<span>03:00PM</span></div><div class="pic" role="img" aria-label="Marathon runners"></div><div class="info">Annual Merathon 2020 for Donation<small>Mayor office,new joursy</small></div></div>
  <div class="item"><div class="date">30 NOV 2020<span>03:00PM</span></div><div class="pic" role="img" aria-label="Marathon runners"></div><div class="info">Annual Merathon 2020 for Donation<small>Mayor office,new joursy</small></div></div>
</div>

<!-- blog -->
<div class="abs blog-kicker heading">Blog</div>
<h2 class="abs blog-title">Our News</h2>
<div class="photo post" style="left:112px;top:2965px;background:linear-gradient(180deg,#8fb4e0,#a7a487 55%,#9a8f6e)" role="img" aria-label="Farm worker pushing a cart under blue tents"></div>
<div class="post text" style="left:448px;top:2965px"><h3>Protect essential farm workers from deportation, farm worker will urge House Judiciary Committee</h3><div class="date">SEP 23, 2020</div><p>20-year-old farm worker Mateo Ruiz urge the U.S. House Judiciary Committee to recognize the essential contributions of the nation's undocument-ed worker......</p><div class="more">Read More</div></div>
<div class="photo post" style="left:780px;top:2965px;background:linear-gradient(180deg,#a9c3e6,#b9a58d 60%,#8b8b8b)" role="img" aria-label="Workers marching with flags on a road"></div>
<div class="post text" style="left:112px;top:3245px"><h3>Essential WA farm workers to receive more support as CAMPO Foundation unveils emergency relief program during COVID-19</h3><div class="date">SEP 23, 2020</div><p>Recognizing the devastating impact of COVID-19 on Latinos and field workers across the nation and in Washington State, the Campo Foundation—a nonprofit, 501(c)3,</p><div class="more">Read More</div></div>
<div class="photo post" style="left:448px;top:3245px;background:linear-gradient(135deg,#c9e2ef,#8fc3e0 50%,#e9eef2)" role="img" aria-label="Gloved hand holding a coronavirus test tube"></div>
<div class="post text" style="left:780px;top:3245px"><h3>Appeals Court Denies Ag Indus-try Attempt to Stop COVID-19 Testing and Will Consider Amicus Brief by Worker Rights.</h3><div class="date">SEP 23, 2020</div><p>Appeals Court Denies Ag Industry Attempt to Stop COVID-19 Testing and Will Consider Amicus Brief by Worker Rights, Labor......</p><div class="more">Read More</div></div>

<!-- support band -->
<section class="abs band">
  <div class="logo"><div class="dot"></div><b>CAMPO FOUNDATION</b><span>For every Worker</span></div>
  <div class="slogan">Support the rights and well being of every Worker</div>
  <div class="btn">Donate Now</div>
</section>

<!-- stories -->
<section class="stories">
  <div class="photo stories-bg" role="img" aria-label="Faded mural of workers in the background"></div>
  <h2>Worker Stories</h2>
  <div class="photo" style="left:112px;top:4085px;width:475px;height:440px;background:linear-gradient(160deg,#5a4a44,#2f2a2c 60%,#1c1c24)" role="img" aria-label="Woman with glasses speaking in a video post">
    <div class="play" style="left:192px;top:176px;width:86px;height:86px"><svg width="30" height="36" style="left:31px;top:25px"><path d="M0 0L30 18L0 36Z" fill="#2b3fc8"/></svg></div>
  </div>
  <div class="photo" style="left:613px;top:4085px;width:475px;height:220px;background:linear-gradient(150deg,#6e5a4a,#3a3036 60%,#4f5b70)" role="img" aria-label="Video post: The Birth of the Field Workers Union, historic meeting footage">
    <div class="abs" style="left:14px;top:16px;color:#fff;font-size:13px">The Birth of the Field Workers Union</div>
  </div>
  <div class="photo" style="left:613px;top:4325px;width:232px;height:200px;background:linear-gradient(135deg,#d8c7a4,#b99c72)" role="img" aria-label="Social post: Meet the team Monday, portrait of staff member"></div>
  <div class="photo" style="left:862px;top:4325px;width:226px;height:200px;background:linear-gradient(135deg,#f1e7c9,#c9b27c 60%,#4f6fb4)" role="img" aria-label="Social post: community flyer in Spanish"></div>
</section>

<!-- movement partners -->
<div class="abs movement">FARM WORKER MOVEMENT</div>
<div class="badge" style="left:127px;width:60px;border-radius:50%"></div>
<div class="badge" style="left:310px;width:46px;border-radius:50%;background:#888"></div>
<div class="badge" style="left:482px;width:58px;border-radius:50%"></div>
<div class="badge" style="left:612px;width:152px;background:var(--blue);height:52px;top:4774px"></div>
<div class="badge" style="left:838px;width:56px;border-radius:50%;background:#444"></div>
<div class="badge" style="left:998px;width:86px;border-radius:43px 43px 6px 6px;height:48px;top:4778px;background:#a51c1c"></div>

<!-- footer -->
<footer class="abs footer">
  <div class="brand"><div class="dot"></div><div class="name">CAMPO<br>FOUNDATION</div></div>
  <p class="about">The Campo Foundation is a dynamic non-profit organization established in 2006. The Campo Foundation's core purpose is to empower communities to ensure human dignity. We serve over 90,000 immi-grants annually through a holistic ap-proach; we provide critical services and engage our constituents in systemic change to break the cycle of poverty.</p>
  <h4 style="left:560px">Service Link</h4>
  <div class="links">About us<br>Immigraiton<br>Programs<br>Join us<br>Blog<br>Online Support<br>Emergency Support</div>
  <h4 style="left:874px">Information</h4>
  <div class="contact" style="top:136px"><svg width="20" height="28"><path d="M10 0a10 10 0 00-10 10c0 8 10 18 10 18s10-10 10-18A10 10 0 0010 0z" fill="#fff"/><circle cx="10" cy="10" r="4" fill="#232a3e"/></svg><span>1480 Orchard Row, Fresno,<br>CA 93721.</span></div>
  <div class="contact" style="top:190px"><svg width="20" height="18"><path d="M4 1l4 4-2 3a11 11 0 005 5l3-2 4 4-3 3C8 18 1 11 1 4z" fill="#fff"/></svg><span>(559) 410-2256</span></div>
  <div class="contact" style="top:222px"><svg width="24" height="18"><rect x="1" y="2" width="22" height="14" fill="#fff"/><path d="M1 2l11 8 11-8" stroke="#232a3e" stroke-width="1.5" fill="none"/></svg><span>info@campofoundation.org</span></div>
  <div class="social"><span></span><span></span><span></span><span></span></div>
  <div class="copy">©2020 Campo foundation ,All Right Reserved</div>
</footer>

</body>
</html>
```